Land Buying Company Needs Letterhead for Direct Mail Marketing to Land Owners

We are looking for a professional letterhead that we will be including in our direct mail marketing. We will be sending this to land owners who may be interested in selling or purchasing land.

The letterhead needs to be editable. Headers and footers would look nice, but we are open. We would want it to include our address, website, phone, and email info. For right now the address to use for design purposes would the following:

Address: 415 Bramwell Avenue #600
Dallas, TX 75219
Website - www.quillridgeacres.example
Email - info@quillridgeacres.example
Phone - 866-402-ACRE

I have attached our logo zip file that we just had done on Pixel Guild. Let me know what questions you have, and thank you.

```html
<!DOCTYPE html>
<html lang="en">
<head>
<meta charset="utf-8">
<title>Quill Ridge Acres Letterhead</title>
<link href="https://fonts.googleapis.com/css2?family=Montserrat:wght@400;500;600;700&display=swap" rel="stylesheet">
<style>
  :root {
    --forest: #3f6a1e;
    --leaf: #8cc63f;
    --lime: #a6d92a;
    --meadow: #5e8f22;
    --ink: #333333;
    --paper: #ffffff;
  }
  html, body {
    margin: 0;
    padding: 0;
    width: 800px;
    height: 1200px;
    overflow: hidden;
    background: var(--paper);
  }
  .letterhead {
    position: relative;
    width: 800px;
    height: 1200px;
    background: var(--paper);
    font-family: "Montserrat", sans-serif;
    color: var(--ink);
    overflow: hidden;
  }
  .brand {
    position: absolute;
    left: 71px;
    top: 110px;
    display: flex;
    align-items: center;
    gap: 16px;
  }
  .brand-dot {
    width: 70px;
    height: 70px;
    border-radius: 50%;
    background: var(--forest);
  }
  .brand-name {
    font-weight: 700;
    font-size: 22px;
    letter-spacing: 1.5px;
    color: var(--forest);
    line-height: 1;
  }
  .contact {
    position: absolute;
    left: 526px;
    top: 100px;
    font-size: 12.5px;
    line-height: 15px;
    font-style: normal;
  }
  .contact-row {
    display: flex;
    align-items: flex-start;
    gap: 10px;
  }
  .contact-row svg {
    flex: none;
    width: 14px;
    height: 14px;
    fill: var(--leaf);
    margin-top: 1px;
  }
  .contact-phone { font-size: 18px; line-height: 20px; margin-bottom: 6px; }
  .contact-phone svg { margin-top: 3px; }
  .contact-address { margin-bottom: 16px; }
  .subject {
    position: absolute;
    left: 71px;
    top: 284px;
  }
  .subject-title {
    margin: 0;
    font-size: 23px;
    font-weight: 700;
    color: var(--forest);
    letter-spacing: 0.3px;
    line-height: 28px;
  }
  .subject-line {
    margin: 8px 0 0;
    font-size: 14px;
  }
  .body-copy {
    position: absolute;
    left: 71px;
    top: 373px;
    width: 657px;
    font-size: 12px;
    line-height: 14.6px;
    text-align: justify;
  }
  .body-copy p { margin: 0 0 14.6px; }
  .signature {
    position: absolute;
    left: 539px;
    top: 783px;
  }
  .signature-name {
    margin: 0;
    font-size: 12.5px;
    font-weight: 700;
  }
  .signature-line {
    margin: 6px 0 0;
    font-size: 10.5px;
  }
  .footer-band {
    position: absolute;
    left: 0;
    top: 900px;
    width: 800px;
    height: 300px;
    background: linear-gradient(180deg, var(--leaf) 0%, var(--meadow) 40%, var(--forest) 100%);
  }
  .footer-url {
    position: absolute;
    left: 71px;
    top: 1052px;
    font-size: 18px;
    color: var(--paper);
    letter-spacing: 0.4px;
  }
</style>
</head>
<body>
<main class="letterhead">
  <header>
    <div class="brand">
      <span class="brand-dot"></span>
      <span class="brand-name">QUILL RIDGE ACRES</span>
    </div>
    <address class="contact">
      <div class="contact-row contact-phone">
        <svg viewBox="0 0 16 16" aria-hidden="true"><path d="M3 2h3l1.5 3.5-2 1.3a8 8 0 0 0 3.7 3.7l1.3-2L14 10v3a1 1 0 0 1-1 1A11 11 0 0 1 2 3a1 1 0 0 1 1-1z"/></svg>
        <span>866-402-ACRE</span>
      </div>
      <div class="contact-row contact-address">
        <svg viewBox="0 0 16 16" aria-hidden="true"><path d="M8 1a5 5 0 0 1 5 5c0 3.6-5 9-5 9S3 9.6 3 6a5 5 0 0 1 5-5zm0 3a2 2 0 1 0 0 4 2 2 0 0 0 0-4z"/></svg>
        <span>415 Bramwell Avenue #600<br>Dallas, TX 75219</span>
      </div>
      <div class="contact-row">
        <svg viewBox="0 0 16 16" aria-hidden="true"><path d="M1 4h14v9H1zM1.5 4.5 8 9l6.5-4.5" stroke="#fff" stroke-width="1.2"/></svg>
        <span>info@quillridgeacres.example</span>
      </div>
    </address>
  </header>

  <section class="subject">
    <h1 class="subject-title">LOREM IPSUM</h1>
    <p class="subject-line">simply dummy text of the printing</p>
  </section>

  <article class="body-copy">
    <p>Lorem Ipsum is simply dummy text of the printing and typesetting industry. Lorem Ipsum has been the industry's standard dummy text ever since the 1500s, when an unknown printer took a galley of type and scrambled it to make a type specimen book. It has survived not only five centuries, but also the leap into electronic typesetting, remaining essentially unchanged. It was popularised in the 1960s with the release of Typeline sheets containing Lorem Ipsum passages, and more recently with desktop publishing software like PageSmith Studio including versions of Lorem Ipsum.</p>
    <p>It is a long established fact that a reader will be distracted by the readable content of a page when looking at its layout. The point of using Lorem Ipsum is that it has a more-or-less normal distribution of letters, as opposed to using 'Content here, content here', making it look like readable English. Many desktop publishing packages and web page editors now use Lorem Ipsum as their default model text, and a search for 'lorem ipsum' will uncover many web sites still in their infancy. Various versions have evolved over the years, sometimes by accident, sometimes on purpose (injected humour and the like).</p>
    <p>Contrary to popular belief, Lorem Ipsum is not simply random text. It has roots in a piece of classical Latin literature from 45 BC, making it over 2000 years old. Martin Feldwick, a Latin professor at Ashcombe College in Vermont, looked up one of the more obscure Latin words, consectetur, from a Lorem Ipsum passage, and going through the cites of the word in classical literature, discovered the undoubtable source. Lorem Ipsum comes from sections 1.10.32 and 1.10.33 of "de Rebus Agrorum" (On Matters of the Fields) by Varennus, written in 45 BC. This book is a treatise on the theory of ethics, very popular during the Renaissance. The first line of Lorem Ipsum, "Lorem ipsum dolor sit amet..", comes from a line in section 1.10.32.</p>
    <p>The standard chunk of Lorem Ipsum used since the 1500s is reproduced below for those interested. Sections 1.10.32 and 1.10.33 from "de Rebus Agrorum" by Varennus are also reproduced in their exact original form, accompanied by English versions from the 1914 translation by T. Holloway.</p>
  </article>

  <section class="signature">
    <p class="signature-name">LOREM IPSUM</p>
    <p class="signature-line">simply dummy text of the printing</p>
  </section>

  <footer>
    <div class="footer-band" role="img" aria-label="Green landscape footer band with pine tree silhouettes and two small birds"></div>
    <div class="footer-url">www.quillridgeacres.example</div>
  </footer>
</main>
</body>
</html>
```